New Bottle Label for our Velindor Grand Reserva Brandy

Graphic Design Brief
We need a new bottle label for our Brandy Gran Reserva that we want to bring to the market.
Please have a look at all our current bottles and labels and the feel of our company under www.velindor-example.ch. We would like the design to be still different to the rest - as it is not a whisky, not a fruit product, not a spirit like a gin, thus we need to create like a new family, but still fitting in with the rest of the products.
The bottle that we will be using for the brand is a different one than the one that we already have, the design of the bottle is attached with a document.
I have also attached a briefing in regards to Brandy in general for your information.
### 1. What is Brandy?
Brandy is a distilled spirit made from fermented wine or other fruit wines. It is traditionally aged in oak barrels, which gives it its characteristic color and rich flavor. The aging process in oak is essential for developing the aromas and quality of the brandy.
### 2. What is Brandy Reserva?
A Brandy labeled as "Reserva" has undergone a longer aging process, typically at least 2 to 3 years, in oak barrels. This aging gives the brandy a deeper, more complex flavor profile and a darker color. "Reserva" is often an indication of higher quality.
### 3. Who enjoys drinking Brandy?
Brandy is typically favored by those who appreciate a deep, rich tasting experience. This often includes older consumers who value the time-aged complexity of the spirit. However, Brandy is also gaining popularity among younger people, especially through cocktails and modern serving styles.
### 4. Why is Brandy trending?
Brandy is experiencing a resurgence as consumers increasingly value quality and artisanal production methods. Its versatility in cocktails and association with traditional, luxurious experiences have also contributed to its renewed popularity.
### 5. What colors would be associated with Brandy?
The typical colors associated with Brandy are warm gold, amber, and deep golden-brown tones. These colors reflect the aging process in oak barrels and the richness of the flavors. Other associated colors might include dark brown and mahogany.
### 6. What is important to customers when buying Brandy?
Customers care about the origin of the Brandy, the aging time, the quality of the ingredients, the production method, and the brand. They also pay attention to the prestige of the product and the authenticity of the production.
### 7. What is not important to customers when buying Brandy?
For many customers, the price and packaging (unless it’s especially exclusive) may be less important than the quality and taste of the Brandy. The distillery name might be less significant if it isn’t tied to a particular reputation.
### 8. What do customers know about Swiss Brandy?
Swiss Brandy is still relatively unknown in many markets, but customers who are familiar with it appreciate the precision and quality of Swiss production. Swiss Brandy is assumed to be made with care and under strict quality standards.
### 9. What is Brandy Gran Reserva?
**Brandy Gran Reserva** is an even higher quality and longer-aged version of Brandy. Generally, a Gran Reserva is aged for at least 5 to 10 years or more in oak barrels. This extended aging process gives the Brandy an especially deep, complex flavor profile and often a darker, richer color. Gran Reserva is often regarded as the top-tier product within a Brandy range and appeals to discerning consumers who value quality, refinement, and a luxurious tasting experience.
The label “Gran Reserva” thus indicates the highest quality level for Brandies, similar to other spirits (like wine or whisky), where the aging time is a critical factor.
We age our Brandy Gran Reserva in the Solara way.
### 10. What emotions are associated with Brandy?
Brandy is often associated with luxury, relaxation, and comfort. It evokes feelings of tradition, elegance, and sophistication. Drinking Brandy is frequently seen as a moment of reflection and enjoyment.
### 11. How should Brandy be marketed?
Brandy should be marketed with a focus on its artisanal production, quality, and tradition. A narrative around the product, its aging, and origin can help create an emotional connection with the customer. The marketing should also emphasize the versatility of Brandy, whether consumed neat or in cocktails.
**Label design**:
The label should reflect the exclusivity of the product, with an elegant, minimalist design. The label should include information about the aging time, the use of oak barrels, and a brief story about the Brandy’s production.
we would like to have a modern look to the whole deisgn of the brandy
Target Market(s)
Customers that like Brandy
Target Market(s)
Switzerland
Industry/Entity Type
Distillery
Look and feel

```html
<!DOCTYPE html>
<html lang="en">
<head>
<meta charset="utf-8">
<title>Velindor Gran Reserva – Bottle Label</title>
<link rel="stylesheet" href="https://fonts.googleapis.com/css2?family=Marcellus&display=swap">
<style>
  :root {
    --amber-light: #d9732f;
    --amber: #b8501a;
    --amber-deep: #7a2e0c;
    --seal-red: #8c0b0b;
    --seal-red-dark: #6e0707;
    --ink: #ffffff;
    --font-label: "Marcellus", serif;
  }
  html, body {
    margin: 0;
    padding: 0;
    width: 1200px;
    height: 1200px;
    overflow: hidden;
  }
  .label {
    position: relative;
    width: 1200px;
    height: 1200px;
    background: radial-gradient(ellipse at 50% 45%, var(--amber-light) 0%, var(--amber) 45%, var(--amber-deep) 100%);
    color: var(--ink);
    font-family: var(--font-label);
  }
  .brand-name {
    position: absolute;
    top: 78px;
    left: 0;
    width: 100%;
    margin: 0;
    text-align: center;
    font-size: 120px;
    font-weight: 400;
    line-height: 1;
    letter-spacing: 2px;
  }
  .category {
    margin: 0;
    padding: 0;
  }
  .category span {
    position: absolute;
    left: 0;
    width: 100%;
    text-align: center;
    text-transform: uppercase;
    line-height: 1;
  }
  .category .origin { top: 264px; font-size: 42px; letter-spacing: 7px; }
  .category .tier   { top: 320px; font-size: 42px; letter-spacing: 4px; }
  .category .spirit { top: 371px; font-size: 58px; letter-spacing: 7px; }
  .seal {
    position: absolute;
    left: 260px;
    top: 434px;
    width: 680px;
    height: 680px;
  }
  .seal text { fill: var(--ink); font-family: var(--font-label); }
</style>
</head>
<body>
<main class="label">
  <h1 class="brand-name">Velindor</h1>

  <p class="category">
    <span class="origin">Swiss</span>
    <span class="tier">Premium</span>
    <span class="spirit">Brandy</span>
  </p>

  <svg class="seal" viewBox="0 0 680 680" xmlns="http://www.w3.org/2000/svg" aria-label="Gran Reserva seal">
    <defs>
      <radialGradient id="seal-fill" cx="50%" cy="45%" r="60%">
        <stop offset="0%" stop-color="#8c0b0b"/>
        <stop offset="100%" stop-color="#6e0707"/>
      </radialGradient>
      <path id="arc-aged" d="M 250 490 A 110 110 0 0 1 430 490"/>
      <path id="arc-years" d="M 250 588 A 110 110 0 0 0 430 588"/>
    </defs>

    <circle class="seal-disc" cx="340" cy="340" r="340" fill="url(#seal-fill)"/>

    <text class="seal-title" x="340" y="116" text-anchor="middle" font-size="100" textLength="272" lengthAdjust="spacingAndGlyphs">GRAN</text>
    <text class="seal-title" x="340" y="238" text-anchor="middle" font-size="100" textLength="427" lengthAdjust="spacingAndGlyphs">RESERVA</text>

    <text class="seal-method" x="340" y="326" text-anchor="middle" font-size="32" textLength="326" lengthAdjust="spacing">OAK BARREL</text>
    <text class="seal-method" x="340" y="378" text-anchor="middle" font-size="30" textLength="180" lengthAdjust="spacing">SOLARA</text>

    <text class="seal-age-word" font-size="26" letter-spacing="3">
      <textPath href="#arc-aged" startOffset="50%" text-anchor="middle">AGED</textPath>
    </text>
    <text class="seal-age" x="340" y="578" text-anchor="middle" font-size="150">5</text>
    <text class="seal-age-word" font-size="26" letter-spacing="3">
      <textPath href="#arc-years" startOffset="50%" text-anchor="middle">YEARS</textPath>
    </text>

    <line x1="246" y1="483" x2="246" y2="571" stroke="#ffffff" stroke-width="2.5"/>
    <line x1="428" y1="483" x2="428" y2="571" stroke="#ffffff" stroke-width="2.5"/>

    <text class="seal-volume" x="186" y="516" text-anchor="middle" font-size="22" letter-spacing="6">50</text>
    <text class="seal-volume" x="186" y="545" text-anchor="middle" font-size="22" letter-spacing="6">CL</text>

    <text class="seal-strength" x="501" y="510" text-anchor="middle" font-size="22" letter-spacing="5">54%</text>
    <text class="seal-strength" x="501" y="540" text-anchor="middle" font-size="22" letter-spacing="5">VOL.</text>
  </svg>
</main>
</body>
</html>
```